Tovlen Systems New Website - IT Infrastructure | Smart Cabinet | Micro Data Center

We're an IT SI providing Server Room Design & Build | All-in-One Rack & Smart Cabinet | Structured Cabling | IT Relocation | Maintenance. Old website can be found at www.tovlensys.com.hk. We'd like a brand new wix website which is modern, minimalist, interactive with some animation. Website content will be mostly static and include our service, our project, news and events, about us, contacts, blogs, partners and brands, etc.

reference sites:
We'd like to see more designs referring to below

https://www.pixelbazar.example/design/51730264
https://www.pixelbazar.example/design/51869047
https://vellhorn.example/

Animation (scrolling effect) referring to
https://vellhorn.example/intelligence/smart-office-room/
Updates

we'd like below style.

Designs look the same

Target Market(s)

Commercials in HK

Industry/Entity Type

IT, Technology, Data Center

Coding

Coded - Design and coding required

Font styles to use
Sans Serif

Requirements
Must have
• CMS, Some Interactive Elements/ Graphics

```html
<!DOCTYPE html>
<html lang="en">
<head>
<meta charset="utf-8">
<title>Tovlen Systems – IT Infrastructure</title>
<link href="https://fonts.googleapis.com/css2?family=Lexend:wght@400;500;600&family=Inter:wght@400;500;600&display=swap" rel="stylesheet">
<style>
:root{
  --navy:#1b1b40;
  --navy-card:#20204a;
  --navy-deep:#17173a;
  --input:#2d2d63;
  --teal:#15a68f;
  --teal-light:#37c3ad;
  --blue:#0e5cb8;
  --white:#ffffff;
  --line:#3a3a6a;
  --footer-text:#a9acd0;
}
*{margin:0;padding:0;box-sizing:border-box}
html,body{width:1200px;height:3477px;overflow:hidden}
body{position:relative;background:var(--navy);color:var(--white);font-family:"Inter",sans-serif}
.abs{position:absolute}
h1,h2,h3{font-family:"Lexend",sans-serif;font-weight:500}
.eyebrow{font-size:11px;letter-spacing:3px;font-weight:600;color:#cfd2ec;text-transform:uppercase}
.btn{position:absolute;display:flex;align-items:center;justify-content:center;font-size:15px;font-weight:500;color:var(--white);border-radius:3px}

/* hero */
.hero{position:absolute;left:0;top:0;width:1200px;height:615px;background:radial-gradient(ellipse at 80% 20%,#2f8a96 0%,#1d5d73 35%,#143c56 70%,#10304a 100%)}
.hero-photo{position:absolute;inset:0;background:linear-gradient(135deg,rgba(70,170,180,.25),rgba(10,40,60,.1) 60%,rgba(60,150,170,.2))}
.brand{position:absolute;display:flex;align-items:center;gap:10px;font-family:"Lexend",sans-serif;font-weight:500;color:var(--white)}
.brand .mark{border:3px solid var(--white);border-radius:3px}
.nav a{position:absolute;top:50px;font-size:14px;color:var(--white);text-decoration:none}
.nav .active{color:var(--teal-light);border-bottom:2px solid var(--teal-light);padding-bottom:4px}
.nav .cta{left:1010px;top:44px;width:111px;height:28px;background:var(--white);color:var(--teal);border-radius:3px;display:flex;align-items:center;justify-content:center}
.hero-copy{position:absolute;left:0;top:205px;width:1200px;text-align:center}
.hero-copy h1{font-size:40px;line-height:47px;margin-top:10px}

/* partners */
.partners{position:absolute;left:0;top:615px;width:1200px;height:70px;background:var(--white);display:flex;align-items:center;justify-content:center;gap:22px}
.partner{width:62px;height:14px;background:#c7cad6;border-radius:3px}

/* about */
.about h2{font-size:34px;line-height:41px}
.about-text{position:absolute;left:83px;top:974px;width:450px}
.about-text p{font-size:13px;line-height:17.5px;color:#e8e9f6}
.about-text p + p{margin-top:17px}

/* services */
.card{position:absolute;top:1702px;width:203px;height:211px;border:1px solid var(--line);border-radius:6px;background:var(--navy);text-align:center}
.card .icon{width:82px;height:82px;border-radius:50%;background:#2c2d5e;margin:33px auto 0;position:relative;display:flex;align-items:center;justify-content:center}
.card .num{position:absolute;right:-2px;top:-2px;width:20px;height:20px;border-radius:50%;background:#1ea3df;font-size:9px;display:flex;align-items:center;justify-content:center}
.card h3{font-size:19px;line-height:24px;margin-top:18px}
.card.active{top:1686px;left:356px;width:193px;height:242px;background:var(--teal);border:none;text-align:left;padding:26px 14px 0 30px}
.card.active h3{text-align:center;margin:0 0 12px -16px;font-size:18px;line-height:24px;white-space:nowrap}
.card.active p{font-size:12.5px;line-height:17.5px}

/* projects */
.project{position:absolute;top:2073px;width:300px;height:215px;background:linear-gradient(180deg,#1f5a86 0%,#2a7fa3 45%,#2aa49a 100%)}
.project .title{position:absolute;left:20px;top:134px;border-left:3px solid var(--teal-light);padding-left:8px;font-family:"Lexend",sans-serif;font-size:19px;line-height:24px;font-weight:500;white-space:nowrap}
.project .loc{position:absolute;left:30px;top:188px;font-size:12px;background:rgba(255,255,255,.18);padding:1px 6px;border-radius:3px}

/* contact */
.contact{position:absolute;left:233px;top:2368px;width:739px;height:712px;background:var(--navy-card);border-radius:14px}
.field-label{position:absolute;font-size:12.5px}
.field{position:absolute;height:49px;background:var(--input);border-radius:3px;font-size:10px;color:#8387b4;padding:18px 7px}

/* footer */
.footer{position:absolute;left:0;top:3155px;width:1200px;height:322px;background:var(--navy-deep)}
.footer p,.footer a{font-size:13px;line-height:20px;color:var(--footer-text);text-decoration:none;display:block}
.footer h4{font-size:13px;font-weight:600;margin-bottom:8px}
.social{display:flex;gap:9px}
.social span{width:15px;height:15px;border-radius:50%;background:var(--footer-text)}
</style>
</head>
<body>

<section class="hero">
  <div class="hero-photo" role="img" aria-label="Upward view of a modern glass building facade in teal tones"></div>
  <div class="brand" style="left:83px;top:35px;font-size:30px"><span class="mark" style="width:34px;height:34px"></span>Tovlen</div>
  <nav class="nav">
    <a class="active" style="left:591px">Home</a>
    <a style="left:669px">About Us</a>
    <a style="left:768px">Our Services</a>
    <a style="left:891px">Our Projects</a>
    <a class="cta">Contact Us</a>
  </nav>
  <div class="hero-copy">
    <div class="eyebrow">Future-ready IT ecosystems</div>
    <h1>Elevate your business<br>with Tovlen Systems' comprehensive<br>IT infrastructure services.</h1>
  </div>
  <a class="btn" style="left:425px;top:386px;width:160px;height:51px;background:var(--blue)">Contact Us</a>
  <a class="btn" style="left:626px;top:386px;width:161px;height:51px;background:var(--teal)">Learn More</a>
</section>

<div class="partners" aria-label="Partner brands">
  <span class="partner"></span><span class="partner"></span><span class="partner"></span><span class="partner"></span><span class="partner"></span><span class="partner"></span><span class="partner"></span><span class="partner"></span><span class="partner"></span><span class="partner"></span><span class="partner"></span><span class="partner"></span><span class="partner"></span><span class="partner" style="width:20px;height:24px"></span>
</div>

<section class="about">
  <svg class="abs" style="left:0;top:685px" width="1200" height="1390" viewBox="0 0 1200 1390" aria-hidden="true">
    <g fill="none" stroke="#2a6a9a" stroke-width="2">
      <path d="M120 50 L138 40 L138 62 Z"/><path d="M376 125 L396 125 L384 142 Z"/><path d="M996 87 L1016 87 L1004 104 Z"/><path d="M734 840 L752 832 L750 850 Z"/><path d="M904 1277 L924 1277 L912 1294 Z"/>
    </g>
    <g fill="#1e6fa6"><circle cx="309" cy="19" r="2.5"/><circle cx="846" cy="75" r="2.5"/><circle cx="415" cy="820" r="2.5"/><circle cx="292" cy="887" r="2.5"/><circle cx="1057" cy="840" r="2.5"/></g>
  </svg>
  <div class="abs eyebrow" style="left:83px;top:839px">Who are we</div>
  <h2 class="abs" style="left:83px;top:855px">About<br>Tovlen Systems</h2>
  <div class="about-text">
    <p>Tovlen Systems is well experienced in delivering the best in Data Center Infrastructure, Network Infrastructure, Structured Cabling, Telephony, Access Control, Video Surveillance, Audiovisual &amp; Conferencing, Relocation &amp; Migration and Maintenance solutions. Our dedication, focus, and expertise wins much recognition of many IT professionals in all industries in the region. In Tovlen Systems's Belief, the major reason that we gain a lot of true long-lasting business relationship with our clients was that we offer them the attention, consideration, passion, and professionalism that they deserved.</p>
    <p>With our vendor-independent expertise in best-of-breed IT infrastucture solution, not only are we to fulfill your business needs with unbiased recommendation, but we also help IT Professionals create the most cost-effective solution and best uptime that meets their ever-changing demand.</p>
  </div>
  <a class="btn" style="left:83px;top:1288px;width:157px;height:51px;background:var(--blue)">Read More</a>
  <div class="abs" role="img" aria-label="Data center aisle lined with server racks glowing blue" style="left:647px;top:865px;width:317px;height:323px;background:linear-gradient(160deg,#7fc8d8 0%,#2d6f8e 45%,#143a58 100%)"></div>
</section>

<section class="services">
  <div class="abs eyebrow" style="left:0;top:1548px;width:1200px;text-align:center">Our services</div>
  <h2 class="abs" style="left:0;top:1562px;width:1200px;text-align:center;font-size:35px;line-height:41px">Comprehensive<br>Technology Solutions</h2>
  <div class="card" style="left:115px">
    <div class="icon"><span class="num">01</span><svg width="34" height="40" viewBox="0 0 34 40" fill="#fff"><ellipse cx="17" cy="6" rx="15" ry="5"/><rect x="2" y="12" width="30" height="8" rx="3"/><rect x="2" y="22" width="30" height="8" rx="3"/><rect x="2" y="32" width="30" height="7" rx="3"/></svg></div>
    <h3>Data Center<br>Design and Build</h3>
  </div>
  <div class="card active">
    <h3>Structured Cable &amp;<br>fiber backbone</h3>
    <p>Future-proof your connectivity with robust structured cabling systems, ensuring seamless support for voice, data, video, security, and more...</p>
    <svg class="abs" style="left:193px;top:203px" width="22" height="24" viewBox="0 0 22 24"><path d="M2 2 L20 12 L12 13 L8 21 Z" fill="#111" stroke="#fff" stroke-width="1.5"/></svg>
  </div>
  <div class="card" style="left:626px">
    <div class="icon"><span class="num">03</span><svg width="34" height="34" viewBox="0 0 34 34" stroke="#fff" stroke-width="3" stroke-linecap="round"><path d="M6 28 L28 6"/><path d="M6 6 L28 28"/></svg></div>
    <h3>All-in-One Rack/<br>Micro-Data Center</h3>
  </div>
  <div class="card" style="left:882px">
    <div class="icon"><span class="num">04</span><svg width="44" height="38" viewBox="0 0 44 38" fill="none" stroke="#fff" stroke-width="2.2"><rect x="3" y="3" width="20" height="14"/><rect x="21" y="19" width="20" height="14"/><path d="M13 17 V24 H21"/></svg></div>
    <h3>Audiovisual &amp;<br>Conference Room</h3>
  </div>
</section>

<section class="projects">
  <div class="project" style="left:0" role="img" aria-label="Server rack with blue network cabling"><div class="title">A renowned China based<br>listed insurance company</div><div class="loc">⌖ Kowloon</div></div>
  <div class="project" style="left:300px" role="img" aria-label="Patch panels with bundled blue cables"><div class="title">GLOBEVENT SOURCING:<br>Server Room Setup</div><div class="loc">⌖ Hong Kong</div></div>
  <div class="project" style="left:600px" role="img" aria-label="Server room with dark cabinets"><div class="title">Harbourline Capital &amp;<br>Meridia Life</div><div class="loc">⌖ Hong Kong</div></div>
  <div class="project" style="left:900px" role="img" aria-label="Rack cabinets in a securities firm data room"><div class="title">A renowned China based<br>Securities firm</div><div class="loc">⌖ Hong Kong</div></div>
</section>

<section class="contact">
  <div class="abs eyebrow" style="left:0;top:58px;width:739px;text-align:center">Contact us</div>
  <h2 class="abs" style="left:0;top:72px;width:739px;text-align:center;font-size:33px">Take the First Step</h2>
  <p class="abs" style="left:0;top:115px;width:739px;text-align:center;font-size:13.5px;line-height:18px">Complete the form below to get in touch with Tovlen Systems.<br>We will be glad to answer your questions as soon as possible.</p>
  <span class="field-label" style="left:99px;top:198px">First Name</span>
  <div class="field" style="left:99px;top:221px;width:258px">Enter your first name</div>
  <span class="field-label" style="left:378px;top:198px">Last Name</span>
  <div class="field" style="left:378px;top:221px;width:258px">Enter your last name</div>
  <span class="field-label" style="left:99px;top:308px">Phone Number</span>
  <div class="field" style="left:99px;top:331px;width:258px">Enter phone number with country code</div>
  <span class="field-label" style="left:378px;top:308px">Email</span>
  <div class="field" style="left:378px;top:331px;width:258px">Enter your email address</div>
  <span class="field-label" style="left:99px;top:418px">Questions</span>
  <div class="field" style="left:99px;top:442px;width:537px;height:63px;padding-top:8px">Ask your questions here...</div>
  <svg class="abs" style="left:101px;top:537px" width="15" height="15" viewBox="0 0 15 15"><rect width="15" height="15" rx="2" fill="#8a66c9"/><path d="M3.5 7.5 L6.5 10.5 L11.5 4.5" stroke="#fff" stroke-width="1.8" fill="none"/></svg>
  <span class="abs" style="left:130px;top:537px;font-size:11.5px">By sending this form I confirm that I have read and accept the <b>Privacy Policy</b></span>
  <a class="btn" style="left:101px;top:601px;width:535px;height:50px;background:var(--blue)">Submit</a>
</section>

<footer class="footer">
  <div class="brand" style="left:83px;top:50px;font-size:40px"><span class="mark" style="width:46px;height:46px"></span>Tovlen</div>
  <div class="abs" style="left:83px;top:140px"><p>Rm 1208, 12/F, Lumen Tech Plaza, 18 Kai Fong Street,<br>San Po Kong, Kowloon, Hong Kong</p></div>
  <div class="abs" style="left:83px;top:212px"><p>T. +852 2000 1480 / +852 5000 3716<br>E. marketing@tovlensys.com.hk<br>F. +852 3000 2274</p></div>
  <div class="abs" style="left:590px;top:105px"><h4>Quick Links</h4><a>Home</a><a style="margin-top:6px">About Us</a><a style="margin-top:6px">Our Services</a><a style="margin-top:6px">Our Projects</a><a style="margin-top:6px">Contact Us</a></div>
  <div class="abs" style="left:830px;top:105px"><h4>Others</h4><a>Privacy Policy</a><a style="margin-top:6px">Cookie Policy</a><a style="margin-top:6px">Terms &amp; Conditions</a></div>
  <div class="abs" style="left:1027px;top:100px"><h4>Social</h4><div class="social"><span></span><span></span><span></span><span></span></div></div>
  <div class="abs" style="left:0;top:296px;width:1200px;text-align:center;font-size:10px;color:var(--footer-text)">© 2023 Tovlen Systems . All Rights Reserved.</div>
</footer>

</body>
</html>
```